Parenting Teens Book Cover Design Project

Updating my existing cover (see attached) so that it is more modern/contemporary.
The book is for Australian parents about helping their teens through their senior years of school and covers info about helping them with motivation, stress, school, parties, career decisions, conflict etc. The author (myself) is a clinical psychologist who specialises in working with teens. I sell this book through my website - see www.brightquillpress.net -(so a small version of the cover in the products section of my site still needs to look good) and back of room sales. I've sold a few thousand of these over the last 9 years but the current cover feels dated to me.
I'm looking for something with clean lines, not cluttered, modern and bold. I'm wary of teen/parent images that look "happy American sitcom" (sorry if this offends).
I've had another self published book which had an entirely black glossy cover and while this looked great, it was a nightmare to sell because the covers got very easily scratched and with faded bits.
It will be an a5 size book.
There is possibly too much font on the back cover, if it cant be made to look good, I will try to reduce it.
Please note, I am a genuine seeker, and am keen to get this design from this website, and will only go elsewhere if I really cant find what I'm looking for here.
Parents and secondary teachers
School

```html
<!DOCTYPE html>
<html lang="en">
<head>
<meta charset="utf-8">
<title>The Years that Matter – Book Cover</title>
<link rel="stylesheet" href="https://fonts.googleapis.com/css2?family=Figtree:wght@400;700;800&display=swap">
<style>
  :root {
    --paper: #ffffff;
    --ink: #1d1b1c;
    --plum-deep: #8c2468;
    --plum: #a9447f;
    --blush: #e6cfdb;
    --mist: #f5f1f3;
    --white-soft: #fcfbfb;
  }
  html, body {
    margin: 0;
    padding: 0;
    overflow: hidden;
    background: var(--paper);
  }
  .cover {
    position: relative;
    width: 846px;
    height: 1200px;
    background: var(--paper);
    overflow: hidden;
    font-family: "Figtree", "Helvetica Neue", Arial, sans-serif;
    color: var(--ink);
  }
  .cover-photo {
    position: absolute;
    left: 0;
    top: 392px;
    width: 846px;
    height: 808px;
    background:
      linear-gradient(180deg, var(--paper) 0%, rgba(255,255,255,0) 14%),
      linear-gradient(100deg, var(--plum-deep) 0%, var(--plum) 20%, var(--blush) 44%, var(--mist) 64%, var(--white-soft) 100%);
    z-index: 0;
  }
  .edition {
    position: absolute;
    left: 56px;
    top: 56px;
    margin: 0;
    font-size: 21px;
    font-weight: 400;
    z-index: 1;
  }
  .author {
    position: absolute;
    left: 386px;
    top: 116px;
    margin: 0;
    font-size: 27px;
    font-weight: 700;
    z-index: 1;
  }
  .book-title {
    position: absolute;
    left: 383px;
    top: 170px;
    margin: 0;
    font-size: 82px;
    font-weight: 800;
    line-height: 76px;
    letter-spacing: -0.5px;
    white-space: nowrap;
    z-index: 1;
  }
  .subtitle {
    position: absolute;
    left: 386px;
    top: 355px;
    margin: 0;
    font-size: 25px;
    font-weight: 700;
    line-height: 28px;
    white-space: nowrap;
    z-index: 1;
  }
</style>
</head>
<body>
  <main class="cover">
    <div class="cover-photo" role="img" aria-label="Photograph of a mother in a magenta top with folded arms turned away from her downcast teenage daughter in white, on a white background"></div>
    <p class="edition">Third Edition</p>
    <p class="author">Maren Holloway</p>
    <h1 class="book-title">The Years<br>that Matter</h1>
    <p class="subtitle">Maximise Motivation, Grades<br>and Optimism in Your Senior<br>School Student</p>
  </main>
</body>
</html>
```